Vegan Alfredo Sauce Label Design for Brambleway Pantry Co

We are a food co. committed to making vegan food more accessible to people who want to eat healthier. Our first line of product is vegan Alfredo sauce.
We have 3 flavors:
- Garlic
- Pesto
- Lemony Artichoke
The current project is the design for the first flavor: garlic. However, we would like a template that would translate well to other flavors, so they look like a family of products.
These will be in standard 16 oz jars. The whole label will be approx 6cm x 24cm, but the front visual space is approx 6cm x 10cm. The rest will be nutritional labeling and copy about the company.
We also need a stamp or font- based logo that says Brambleway Pantry Co. (or lower case: brambleway pantry co.), the name of the company.
The picture (attached) of Plantbased Nacho Dip is the closest to what we are going for. Because the sauce is creamy white, a colorful background with off-white font will be best.
We currently have a website, although we are doing a brand over-haul (hence, this posting) www.bramblewaypantryco.example. If the designer is a good fit, we have several more projects, in line.
Other brands we love: Tidewell Grocers, Marlow Ridge Provisions, Pulp Poured Daily.
The final brand should communicate hip, natural and health.
And personally, I love design that is clever and somehow makes me smile.
Target Market(s)
Vegans, vegetarians, and people with common food allergies - all ages.
Young, hip families.
Industry/Entity Type
It Company
Requirements
Must have
- Copy:
Vegan Alfredo or Vegan Alfredo Sauce
Garlic
Brambleway Pantry or Brambleway Pantry Co
16 oz
Nice to have
- May include copy:
Gluten-Free Soy-Free Nut-Free
Should not have
- Neon colors

```html
<!DOCTYPE html>
<html lang="en">
<head>
<meta charset="utf-8">
<title>Vegan Alfredo Sauce – Garlic – Brambleway Pantry Co</title>
<link rel="stylesheet" href="https://fonts.googleapis.com/css2?family=Yellowtail&family=Dancing+Script:wght@500&family=Roboto+Slab:wght@300&family=Oswald:wght@300&display=swap">
<style>
  :root {
    --page: #ffffff;
    --bark: #6e6253;
    --bark-deep: #524638;
    --sage: #7aab72;
    --sage-deep: #6b9b63;
    --orange: #f39322;
    --cream: #ffffff;
    --mist: #dcdadb;
    --ink: #2b2622;
    --charcoal: #403c3b;
    --sand: #c9b79a;
    --dot: #5c6a5e;
  }
  html, body {
    margin: 0;
    width: 1200px;
    height: 1100px;
    overflow: hidden;
    background: var(--page);
  }
  .label {
    position: absolute;
    left: 342px;
    top: 265px;
    width: 519px;
    height: 570px;
    overflow: hidden;
  }
  .label__pattern {
    position: absolute;
    inset: 0;
    background: radial-gradient(ellipse at 50% 45%, var(--bark) 0%, var(--bark) 55%, var(--bark-deep) 130%);
  }
  .band {
    position: absolute;
    left: 58px;
    width: 409px;
  }
  .band--product { top: 95px; height: 200px; background: var(--sage); }
  .band--flavour {
    top: 295px; height: 87px; background: var(--orange);
    display: flex; align-items: center; justify-content: center;
  }
  .band--artwork { top: 382px; height: 75px; background: var(--cream); }
  .band--artwork .artwork {
    position: absolute; left: 12px; right: 0; top: 4px; bottom: 8px;
    background: linear-gradient(90deg, var(--mist), #ecebeb 60%, var(--mist));
    border-radius: 4px;
  }
  .band--claims {
    top: 457px; height: 30px; background: var(--charcoal);
    display: flex; align-items: center; justify-content: center;
    font-family: "Roboto Slab", serif; font-weight: 300;
    font-size: 14.5px; letter-spacing: 2.4px; color: var(--sand);
  }
  .product-type {
    position: absolute; left: 58px; width: 409px; top: 210px;
    text-align: center;
    font-family: "Dancing Script", cursive; font-weight: 500;
    font-size: 62px; line-height: 1; color: var(--ink);
  }
  .flavour-name {
    font-family: "Dancing Script", cursive; font-weight: 500;
    font-size: 58px; line-height: 1; color: var(--ink);
    margin-top: -8px;
  }
  .brand-tab {
    position: absolute; left: 161px; top: 487px; width: 202px; height: 46px;
    background: var(--charcoal);
    display: flex; align-items: center; justify-content: center;
    font-family: "Oswald", sans-serif; font-weight: 300;
    font-size: 21px; color: var(--sand); white-space: nowrap;
  }
  .wordmark {
    position: absolute; inset: 0; pointer-events: none;
  }
  .wordmark__text {
    font-family: "Yellowtail", cursive;
    font-size: 158px;
    fill: var(--cream);
    stroke: var(--sage);
    stroke-width: 16px;
    stroke-linejoin: round;
    paint-order: stroke;
  }
</style>
</head>
<body>
  <main class="label">
    <div class="label__pattern" role="img" aria-label="Brown background with dark swirling leaf pattern"></div>

    <div class="band band--product"></div>
    <div class="band band--flavour"><span class="flavour-name">garlic</span></div>
    <div class="band band--artwork">
      <div class="artwork" role="img" aria-label="Row of five garlic bulb illustrations on a light grey brush stroke"></div>
    </div>
    <div class="band band--claims">gluten-free · soy-free · nut-free</div>

    <svg class="wordmark" width="519" height="570" viewBox="0 0 519 570" aria-hidden="true">
      <line x1="78" y1="193" x2="450" y2="193" stroke="var(--dot)" stroke-width="4.5" stroke-linecap="round" stroke-dasharray="0 7.5"/>
      <text class="wordmark__text" x="12" y="180" textLength="430" lengthAdjust="spacingAndGlyphs">Vegan</text>
    </svg>

    <div class="product-type">alfredo sauce</div>

    <div class="brand-tab">Brambleway Pantry Co</div>
  </main>
</body>
</html>
```